Core Investment Strategy's Super Pie Chart

We need a one page visual explanation of an investment strategy we call "Core/Perimeter". This strategy emphasizes a "core" portfolio that will seldom change and "perimeter" investments that will change. Our investment management firm caters to wealthy individuals. We want to project an image of strength and reliability. At the same time, we are willing to explore new concepts. I have uploaded a PDF of my graphically-challenged assistant's attempt at creating the one page visual.

Industry/Entity Type

Investment

```html
<!DOCTYPE html>
<html lang="en">
<head>
<meta charset="utf-8">
<title>Core/Perimeter Portfolio</title>
<link href="https://fonts.googleapis.com/css2?family=Arimo:wght@700&family=Roboto+Condensed:wght@700&display=swap" rel="stylesheet">
<style>
  :root {
    --navy-deep: #0a1f3d;
    --navy-mid: #1a4677;
    --navy-line: #0c2a50;
    --band-light: #f2f2f2;
    --band-shade: #c9c9c9;
    --core-blue: #0a72ba;
    --core-green: #8dc63f;
    --leader-blue: #1b86cf;
    --perimeter-blue: #0a72ba;
    --perimeter-red: #c8203f;
    --perimeter-green: #8dc63f;
    --perimeter-purple: #8e6cb0;
    --ink-light: #ffffff;
    --ink-dark: #1b2a3d;
  }
  * { margin: 0; padding: 0; box-sizing: border-box; }
  html, body { width: 1200px; height: 848px; overflow: hidden; background: var(--navy-deep); }
  .poster {
    position: relative;
    width: 1200px;
    height: 848px;
    overflow: hidden;
    background: radial-gradient(ellipse 640px 460px at 600px 400px, var(--navy-mid) 0%, #143a66 45%, var(--navy-deep) 100%);
    font-family: "Arimo", Arial, sans-serif;
  }
  .title-band {
    position: absolute; left: 0; top: 0; width: 1200px; height: 51px;
    background: linear-gradient(to bottom, var(--band-light), var(--band-shade));
    display: flex; align-items: center; justify-content: center;
  }
  .title-band h1 {
    font-family: "Roboto Condensed", "Arial Narrow", sans-serif;
    font-weight: 700; font-size: 28px; letter-spacing: 0.5px;
    color: var(--ink-dark);
  }
  .chart { position: absolute; left: 0; top: 0; }
  .label {
    position: absolute; color: var(--ink-light);
    font-size: 13.5px; line-height: 16px; font-weight: 700;
  }
  .label.right { text-align: right; }
  .label.center { text-align: center; }
  .perimeter-key {
    position: absolute; display: flex; align-items: flex-start; gap: 10px;
    color: var(--ink-light); font-size: 14px; line-height: 17px; font-weight: 700;
  }
  .perimeter-key .swatch { width: 24px; height: 24px; flex: none; margin-top: -3px; }
  .legend-band {
    position: absolute; left: 0; top: 757px; width: 1200px; height: 91px;
    background: linear-gradient(to bottom, var(--band-light), var(--band-shade));
    font-family: "Roboto Condensed", "Arial Narrow", sans-serif;
    font-weight: 700; font-size: 25px; color: var(--ink-dark);
    display: flex; flex-direction: column; align-items: center; justify-content: center; gap: 2px;
  }
  .legend-row { display: flex; gap: 22px; letter-spacing: 0.6px; }
  .legend-item { display: flex; align-items: center; gap: 10px; }
  .legend-item .dot { width: 11px; height: 11px; }
  .dot.blue { background: var(--core-blue); }
  .dot.green { background: var(--core-green); }
</style>
</head>
<body>
<div class="poster">
  <header class="title-band"><h1>CORE/PERIMETER PORTFOLIO</h1></header>

  <svg class="chart" width="1200" height="848" viewBox="0 0 1200 848" aria-label="Core portfolio pie chart with perimeter ring">
    <!-- perimeter ring -->
    <g fill="none" stroke-width="33">
      <path d="M654.9,85.8 A316,316 0 0 1 908.1,331.3" stroke="var(--perimeter-blue)"/>
      <path d="M908.1,462.7 A316,316 0 0 1 664.7,706.1" stroke="var(--perimeter-red)"/>
      <path d="M533.3,706.1 A316,316 0 0 1 289.9,462.7" stroke="var(--perimeter-green)"/>
      <path d="M289.9,331.3 A316,316 0 0 1 544.1,85.8" stroke="var(--perimeter-purple)"/>
    </g>
    <!-- core pie -->
    <g stroke="var(--navy-line)" stroke-width="4" stroke-linejoin="round">
      <path class="slice-large-cap" d="M599,397 L599,157 A240,240 0 0 1 768.7,566.7 Z" fill="var(--core-blue)"/>
      <path class="slice-mid-cap" d="M599,397 L768.7,566.7 A240,240 0 0 1 690.8,618.7 Z" fill="var(--core-blue)"/>
      <path class="slice-small-cap" d="M599,397 L690.8,618.7 A240,240 0 0 1 599,637 Z" fill="var(--core-blue)"/>
      <path class="slice-intl" d="M599,397 L599,637 A240,240 0 0 1 429.3,566.7 Z" fill="var(--core-blue)"/>
      <path class="slice-intermediate" d="M599,397 L429.3,566.7 A240,240 0 0 1 429.3,227.3 Z" fill="var(--core-green)"/>
      <path class="slice-short-term" d="M599,397 L429.3,227.3 A240,240 0 0 1 599,157 Z" fill="var(--core-green)"/>
    </g>
    <circle cx="599" cy="397" r="29" fill="#0d2f5c"/>
    <!-- leader lines -->
    <g stroke-width="2">
      <line x1="495" y1="204" x2="263" y2="204" stroke="var(--leader-blue)"/>
      <line x1="423" y1="400" x2="191" y2="400" stroke="var(--leader-blue)"/>
      <line x1="717" y1="300" x2="957" y2="300" stroke="var(--core-green)"/>
      <line x1="713" y1="552" x2="960" y2="520" stroke="var(--core-green)"/>
      <line x1="637" y1="587" x2="933" y2="631" stroke="var(--core-green)"/>
      <line x1="521" y1="587" x2="140" y2="587" stroke="var(--core-green)"/>
    </g>
    <g>
      <circle cx="495" cy="204" r="7" fill="var(--leader-blue)"/>
      <circle cx="423" cy="400" r="7" fill="var(--leader-blue)"/>
      <circle cx="717" cy="300" r="7" fill="var(--core-green)"/>
      <circle cx="713" cy="552" r="7" fill="var(--core-green)"/>
      <circle cx="637" cy="587" r="7" fill="var(--core-green)"/>
      <circle cx="521" cy="587" r="7" fill="var(--core-green)"/>
    </g>
  </svg>

  <div class="label right" style="left:150px; top:177px; width:85px;">Short-Term<br>Bonds,<br>10%</div>
  <div class="label center" style="left:83px; top:382px; width:100px;">Intermediate<br>Bonds,<br>20%</div>
  <div class="label center" style="left:963px; top:285px; width:80px;">Lg. Cap<br>Equities,<br>30%</div>
  <div class="label" style="left:971px; top:513px;">Mid Cap Equities , 5%</div>
  <div class="label" style="left:957px; top:624px;">Sm. Cap Equities, 5%</div>
  <div class="label" style="left:62px; top:572px;">Int'l/Dev.<br>Equities,<br>10%</div>

  <div class="perimeter-key" style="left:263px; top:96px;"><span class="swatch" style="background:var(--perimeter-purple)"></span>Other, 2%</div>
  <div class="perimeter-key" style="left:848px; top:110px;"><span class="swatch" style="background:var(--perimeter-blue)"></span>Alternative Assets, 7%</div>
  <div class="perimeter-key" style="left:176px; top:687px;"><span class="swatch" style="background:var(--perimeter-green)"></span>Attractive Core Assets, 3%</div>
  <div class="perimeter-key" style="left:828px; top:690px;"><span class="swatch" style="background:var(--perimeter-red)"></span>Actively Managed Mutual<br>Funds, 8%</div>

  <footer class="legend-band">
    <div class="legend-row">
      <span class="legend-item"><span class="dot blue"></span>LG. CAP EQUITIES</span>
      <span class="legend-item"><span class="dot blue"></span>MID CAP EQUITIES</span>
      <span class="legend-item"><span class="dot blue"></span>SM. CAP EQUITIES</span>
      <span class="legend-item"><span class="dot blue"></span>INT'L/DEV. EQUITIES</span>
    </div>
    <div class="legend-row">
      <span class="legend-item"><span class="dot green"></span>INTERMEDIATE BONDS</span>
      <span class="legend-item"><span class="dot green"></span>SHORT-TERM BONDS</span>
    </div>
  </footer>
</div>
</body>
</html>
```